QK-Deck Company Powerpoint Template

I would like to create a branded PowerPoint temple that my company can use for all presentations. our website is www.qk-deck-example.com. The company is a software provider for the auto recycling industry (junk yards). Our customers use our software to pull, process, and deliver orders to auto body shops and mechanic shops.
Pages that would be helpful:
Title Page
Content slide
Content slide with image
Workflow/flowchart slide
Image only slide
Final slide

Target Market(s)

Automotive Recycling

Industry/Entity Type

Automotive recycling software

Font styles to use
Sans Serif

Colors
0054AA
0677BA
7BADD7
CADEEF
E8F1F8
FFF300
FFF600
FEFA6F
FFFEC7
FFFEE8

Requirements
Must have
• similarities in other branded items like our website. Title Page, Content slide, Content slide with image, Workflow/flowchart slide, Image only slide, Final slide
Nice to have
• Simple clean design would be preferential

```html
<!DOCTYPE html>
<html lang="en">
<head>
<meta charset="utf-8">
<title>QK-Deck Presentation Template</title>
<link href="https://fonts.googleapis.com/css2?family=Ubuntu:wght@300;400;500;700&display=swap" rel="stylesheet">
<style>
:root{
  --blue:#0054AA; --mid:#0677BA; --light:#7BADD7; --pale:#CADEEF; --mist:#E8F1F8;
  --yellow:#FFF300; --ink:#4a4a4a; --grey:#9a9a9a; --line:#e2e2e2; --page:#eef0f3;
  --photo-warm:linear-gradient(135deg,#8a7358,#b89a72 45%,#5f6f80);
  --photo-cool:linear-gradient(135deg,#6d7a86,#a9b3bb 50%,#4d5a66);
}
*{box-sizing:border-box;margin:0;padding:0}
html,body{width:1200px;height:2261px;overflow:hidden}
body{position:relative;background:var(--page);font-family:"Ubuntu",sans-serif;color:var(--ink)}
.stage{position:absolute;left:0;top:0;width:1200px;height:680px;background:linear-gradient(180deg,#dfe3ea,#eef0f3)}
.hero{position:absolute;left:120px;top:70px;width:375px;height:211px;transform:scale(2.56);transform-origin:0 0;box-shadow:0 2px 8px rgba(0,0,0,.15)}
.slide{position:absolute;width:375px;height:211px;background:#fff;overflow:hidden}
.abs{position:absolute}
.photo{position:absolute;background:var(--photo-warm)}
.photo.cool{background:var(--photo-cool)}
.brand{position:absolute;font-weight:700;color:var(--blue);letter-spacing:-.3px}
.heading{position:absolute;left:22px;top:18px;font-size:14px;font-weight:500;color:var(--blue)}
.heading b{font-weight:700}
.heading::after{content:"";position:absolute;left:0;bottom:-3px;width:26px;height:2px;background:var(--yellow)}
.sub{position:absolute;left:22px;top:44px;font-size:4px;color:#666}
.copy{font-size:4px;line-height:1.35;color:#666}
.copy p{margin-bottom:3px}
.foot{position:absolute;left:10px;right:10px;bottom:5px;height:10px}
.foot .mini{position:absolute;left:0;top:0;font-size:8px;font-weight:700;color:var(--blue)}
.foot .meta{position:absolute;right:0;top:3px;font-size:3.3px;color:#333}
.small-h{font-size:5px;font-weight:500;color:var(--blue)}
.list-row{position:absolute;font-size:7px;color:#555;border-bottom:1px solid var(--line);height:18px;line-height:16px}
.list-row span{color:#c4c4c4;margin-right:10px}
.pill{position:absolute;height:8px;font-size:3.5px;color:#fff;text-align:center;line-height:8px}
</style>
</head>
<body>

<div class="stage"></div>

<!-- featured title slide -->
<div class="hero slide">
  <div class="photo" style="left:150px;top:0;width:225px;height:68px;background:linear-gradient(90deg,#fff,#e6e0d6 50%,#cbbfae)" role="img" aria-label="Warehouse shelving photo, faded"></div>
  <div class="brand" style="left:22px;top:22px;font-size:18px">QK-Deck</div>
  <div class="abs" style="left:0;top:68px;width:375px;height:124px;background:linear-gradient(90deg,#0054AA,#0677BA 70%,#4f87b8)" role="img" aria-label="Blue-tinted warehouse aisle photo"></div>
  <div class="abs" style="left:22px;top:84px;font-size:15px;font-weight:700;color:#fff;line-height:1.15">Transforming<br>Automotive Recycling</div>
  <div class="abs" style="left:22px;top:125px;width:40px;height:2px;background:var(--yellow)"></div>
  <div class="abs" style="left:22px;top:133px;width:200px;font-size:4.6px;color:#fff;line-height:1.25">QK-Deck offers a wide range of consulting services with the necessary tools and expertise to help grow your business.</div>
  <div class="pill" style="left:22px;top:162px;width:72px;background:var(--blue)">www.qk-deck-example.com</div>
  <div class="abs" style="left:195px;top:199px;font-size:3.3px;color:#777">© 2020 by QK-Deck</div>
</div>

<!-- 1 title A -->
<div class="slide" style="left:26px;top:680px">
  <div class="photo" style="left:150px;top:0;width:225px;height:68px;background:linear-gradient(90deg,#fff,#e6e0d6 50%,#cbbfae)" role="img" aria-label="Warehouse shelving photo, faded"></div>
  <div class="brand" style="left:22px;top:22px;font-size:18px">QK-Deck</div>
  <div class="abs" style="left:0;top:68px;width:375px;height:124px;background:linear-gradient(90deg,#0054AA,#0677BA 70%,#4f87b8)" role="img" aria-label="Blue-tinted warehouse aisle photo"></div>
  <div class="abs" style="left:22px;top:84px;font-size:15px;font-weight:700;color:#fff;line-height:1.15">Transforming<br>Automotive Recycling</div>
  <div class="abs" style="left:22px;top:133px;width:200px;font-size:4.6px;color:#fff;line-height:1.25">QK-Deck offers a wide range of consulting services with the necessary tools and expertise to help grow your business.</div>
  <div class="pill" style="left:22px;top:162px;width:72px;background:var(--blue)">www.qk-deck-example.com</div>
  <div class="abs" style="left:195px;top:199px;font-size:3.3px;color:#777">© 2020 by QK-Deck</div>
</div>

<!-- 2 title B -->
<div class="slide" style="left:413px;top:680px">
  <svg class="abs" width="375" height="211" viewBox="0 0 375 211">
    <defs><linearGradient id="gw" x1="0" y1="0" x2="1" y2="1"><stop offset="0" stop-color="#8a7358"/><stop offset=".5" stop-color="#b89a72"/><stop offset="1" stop-color="#5f6f80"/></linearGradient></defs>
    <rect x="140" y="0" width="235" height="211" fill="url(#gw)" role="img" aria-label="Worker on a lift in a warehouse aisle"/>
    <polygon points="140,0 225,0 250,40" fill="var(--mid)" opacity=".9"/>
    <polygon points="0,0 145,0 245,110 135,211 0,211" fill="#fff"/>
    <polygon points="135,211 175,165 215,211" fill="var(--blue)"/>
    <polygon points="175,165 250,211 215,211" fill="var(--mid)"/>
  </svg>
  <div class="brand" style="left:22px;top:34px;font-size:16px">QK-Deck</div>
  <div class="abs" style="left:22px;top:80px;font-size:13px;font-weight:700;color:var(--mid);line-height:1.15">Presentation<br>Title Goes Here!</div>
  <div class="abs" style="left:22px;top:113px;font-size:4px;color:#666">Transforming Automotive Recycling</div>
  <div class="pill" style="left:22px;top:164px;width:62px;background:var(--blue)">December 7, 2022</div>
  <div class="abs" style="left:168px;top:192px;font-size:3px;color:#fff;line-height:1.3">www.qk-deck-example.com<br>©2020 by QK-Deck</div>
</div>

<!-- 3 title C -->
<div class="slide" style="left:800px;top:680px">
  <svg class="abs" width="375" height="211" viewBox="0 0 375 211">
    <defs><linearGradient id="gc" x1="0" y1="0" x2="1" y2="1"><stop offset="0" stop-color="#6d7a86"/><stop offset=".5" stop-color="#a9b3bb"/><stop offset="1" stop-color="#4d5a66"/></linearGradient></defs>
    <rect x="140" y="0" width="235" height="211" fill="url(#gc)" role="img" aria-label="Technician holding a tablet beside an engine"/>
    <polygon points="0,0 150,0 250,105 150,211 0,211" fill="var(--blue)"/>
    <polygon points="150,0 220,0 250,40" fill="var(--mid)" opacity=".9"/>
    <polygon points="150,211 190,168 230,211" fill="var(--light)"/>
  </svg>
  <div class="brand" style="left:22px;top:34px;font-size:16px;color:#fff">QK-Deck</div>
  <div class="abs" style="left:22px;top:80px;font-size:13px;font-weight:700;color:#fff;line-height:1.15">Presentation<br>Title Goes Here!</div>
  <div class="abs" style="left:22px;top:113px;font-size:4px;color:#fff">Transforming Automotive Recycling</div>
  <div class="pill" style="left:22px;top:164px;width:74px;background:var(--light)">December 7, 2022</div>
  <div class="abs" style="left:170px;top:192px;font-size:3px;color:#fff;line-height:1.3">www.qk-deck-example.com<br>©2020 by QK-Deck</div>
</div>

<!-- 4 content -->
<div class="slide" style="left:26px;top:903px">
  <div class="brand" style="left:34px;top:86px;font-size:30px">QK-Deck</div>
  <div class="heading" style="left:200px;top:26px;font-weight:400">Content</div>
  <div class="list-row" style="left:198px;top:64px;width:135px"><span>01</span>Title Goes Here</div>
  <div class="list-row" style="left:198px;top:86px;width:135px"><span>02</span>Title Goes Here</div>
  <div class="list-row" style="left:198px;top:108px;width:135px"><span>03</span>Title Goes Here</div>
  <div class="list-row" style="left:198px;top:130px;width:135px"><span>04</span>Title Goes Here</div>
  <div class="list-row" style="left:198px;top:152px;width:135px"><span>05</span>Title Goes Here</div>
  <div class="foot"><div class="mini">QK-Deck</div><div class="meta">WWW.QK-DECK-EXAMPLE.COM &nbsp;|&nbsp; ©2020 BY QK-DECK &nbsp;|&nbsp; 4</div></div>
</div>

<!-- 5 table of contents -->
<div class="slide" style="left:413px;top:903px">
  <div class="heading" style="font-weight:400">Table of <b>Contents</b></div>
  <div class="list-row" style="left:22px;top:62px;width:135px"><span>01</span>Title Goes Here</div>
  <div class="list-row" style="left:22px;top:84px;width:135px"><span>03</span>Title Goes Here</div>
  <div class="list-row" style="left:22px;top:106px;width:135px"><span>05</span>Title Goes Here</div>
  <div class="list-row" style="left:22px;top:128px;width:135px"><span>07</span>Title Goes Here</div>
  <div class="list-row" style="left:22px;top:150px;width:135px"><span>09</span>Title Goes Here</div>
  <div class="list-row" style="left:178px;top:62px;width:135px"><span>02</span>Title Goes Here</div>
  <div class="list-row" style="left:178px;top:84px;width:135px"><span>04</span>Title Goes Here</div>
  <div class="list-row" style="left:178px;top:106px;width:135px"><span>06</span>Title Goes Here</div>
  <div class="list-row" style="left:178px;top:128px;width:135px"><span>08</span>Title Goes Here</div>
  <div class="list-row" style="left:178px;top:150px;width:135px"><span>10</span>Title Goes Here</div>
  <div class="foot"><div class="mini">QK-Deck</div><div class="meta">WWW.QK-DECK-EXAMPLE.COM &nbsp;|&nbsp; ©2020 BY QK-DECK &nbsp;|&nbsp; 5</div></div>
</div>

<!-- 6 heading text -->
<div class="slide" style="left:800px;top:903px">
  <div class="heading"><b>Heading</b> Goes Here</div>
  <div class="sub">Sub-Heading Goes Here</div>
  <div class="copy abs" style="left:22px;top:68px;width:332px">
    <p>Lorem ipsum dolor sit amet, consectetur adipiscing elit. Vivamus eu dui ex. Curabitur dapibus dignissim dui, in molestie metus feugiat sed. Praesent aliquet lorem ex, eu dapibus odio varius at. Duis eget tellus porta, consequat lacus vitae, venenatis dolor. Nulla facilisi. In et sollicitudin lacus. Donec risus orci, gravida sit amet risus vehicula, aliquet pretium sapien. Nullam sit amet magna non ex bibendum mollis.</p>
    <p>Lorem ipsum dolor sit amet, consectetur adipiscing elit. Vivamus eu dui ex. Curabitur dapibus dignissim dui, in molestie metus feugiat sed. Praesent aliquet lorem ex, eu dapibus odio varius at. Duis eget tellus porta, consequat lacus vitae.</p>
    <p>Donec risus orci, gravida sit amet risus vehicula, aliquet pretium sapien. Nullam sit amet magna non ex bibendum mollis. Nunc vel neque eu augue dignissim congue ut vitae magna. Phasellus eget commodo arcu. Nunc vitae semper dui. Integer venenatis, tellus sit amet interdum pretium, erat neque rhoncus turpis.</p>
  </div>
  <div class="foot"><div class="mini">QK-Deck</div><div class="meta">WWW.QK-DECK-EXAMPLE.COM &nbsp;|&nbsp; ©2020 BY QK-DECK &nbsp;|&nbsp; 6</div></div>
</div>

<!-- 7 column slide -->
<div class="slide" style="left:26px;top:1127px">
  <div class="heading"><b>Column</b> Slide</div>
  <div class="sub">Sub-Heading Goes Here</div>
  <div class="copy abs" style="left:22px;top:60px;width:155px">
    <p>Lorem ipsum dolor sit amet, consectetur adipiscing elit. Vivamus eu dui ex. Curabitur dapibus dignissim dui, in molestie metus feugiat sed. Praesent aliquet lorem ex, eu dapibus odio varius at. Nulla facilisi.</p>
    <p>Nunc placerat, arcu nec mattis fermentum, nisi mauris convallis nunc, ut luctus nunc nisl id ex. Nam semper tristique mauris, et vestibulum leo fringilla vel. Nulla id augue eleifend, egestas ligula et, consequat massa.</p>
    <p>Donec risus orci, gravida sit amet risus vehicula, aliquet pretium sapien. Nullam sit amet magna non ex bibendum mollis. Nunc vel neque eu augue dignissim congue ut vitae magna.</p>
  </div>
  <div class="copy abs" style="left:198px;top:60px;width:155px">
    <p>Lorem ipsum dolor sit amet, consectetur adipiscing elit. Vivamus eu dui ex. Curabitur dapibus dignissim dui, in molestie metus feugiat sed. Praesent aliquet lorem ex, eu dapibus odio varius at. Nulla facilisi.</p>
    <p>Nunc placerat, arcu nec mattis fermentum, nisi mauris convallis nunc, ut luctus nunc nisl id ex. Nam semper tristique mauris, et vestibulum leo fringilla vel. Nulla id augue eleifend, egestas ligula et, consequat massa.</p>
    <p>Donec risus orci, gravida sit amet risus vehicula, aliquet pretium sapien. Nullam sit amet magna non ex bibendum mollis. Nunc vel neque eu augue dignissim congue ut vitae magna.</p>
  </div>
  <div class="foot"><div class="mini">QK-Deck</div><div class="meta">WWW.QK-DECK-EXAMPLE.COM &nbsp;|&nbsp; ©2020 BY QK-DECK &nbsp;|&nbsp; 7</div></div>
</div>

<!-- 8 heading + photo -->
<div class="slide" style="left:413px;top:1127px">
  <div class="heading"><b>Heading</b> Goes Here</div>
  <div class="sub">Sub-Heading Goes Here</div>
  <div class="copy abs" style="left:22px;top:60px;width:170px">
    <p>Lorem ipsum dolor sit amet, consectetur adipiscing elit. Vivamus eu dui ex. Curabitur dapibus dignissim dui, in molestie metus feugiat sed. Praesent aliquet lorem ex, eu dapibus odio varius at.</p>
    <p>Nulla facilisi. In et sollicitudin lacus. Donec risus orci, gravida sit amet risus vehicula, aliquet pretium sapien. Nullam sit amet magna non ex bibendum mollis.</p>
    <p>Nunc vel neque eu augue dignissim congue ut vitae magna. Phasellus eget commodo arcu. Nunc vitae semper dui. Integer venenatis, tellus sit amet interdum pretium.</p>
    <p>Nunc placerat, arcu nec mattis fermentum, nisi mauris convallis nunc, ut luctus nunc nisl id ex. Nam semper tristique mauris, et vestibulum leo fringilla vel.</p>
  </div>
  <div class="photo" style="left:204px;top:19px;width:152px;height:157px" role="img" aria-label="Worker on an order picker in a warehouse aisle"></div>
  <div class="foot"><div class="mini">QK-Deck</div><div class="meta">WWW.QK-DECK-EXAMPLE.COM &nbsp;|&nbsp; ©2020 BY QK-DECK &nbsp;|&nbsp; 8</div></div>
</div>

<!-- 9 products -->
<div class="slide" style="left:800px;top:1127px">
  <div class="heading"><b>Heading</b> Goes Here</div>
  <div class="abs" style="left:20px;top:52px;width:80px;height:30px;border:1px solid var(--line);font-size:9px;font-weight:700;color:#333;text-align:center;line-height:28px">QK Check</div>
  <div class="abs" style="left:106px;top:52px;width:80px;height:30px;border:1px solid var(--line);font-size:9px;font-weight:700;color:#333;text-align:center;line-height:28px">QK Route</div>
  <div class="abs" style="left:192px;top:52px;width:80px;height:30px;border:1px solid var(--line);font-size:9px;font-weight:700;color:#333;text-align:center;line-height:28px">QK Runner</div>
  <div class="abs" style="left:278px;top:52px;width:80px;height:30px;border:1px solid var(--line);font-size:9px;font-weight:700;color:#333;text-align:center;line-height:28px">QK Partner</div>
  <div class="abs" style="left:22px;top:90px;width:74px"><div class="small-h">Heading Goes Here</div><div class="copy" style="margin-top:3px">Donec risus orci, gravida sit amet risus vehicula, aliquet pretium sapien. Nullam sit amet magna non ex bibendum mollis. Nunc vel neque eu augue dignissim congue ut vitae magna.</div></div>
  <div class="abs" style="left:108px;top:90px;width:74px"><div class="small-h">Heading Goes Here</div><div class="copy" style="margin-top:3px">Donec risus orci, gravida sit amet risus vehicula, aliquet pretium sapien. Nullam sit amet magna non ex bibendum mollis. Nunc vel neque eu augue dignissim congue ut vitae magna.</div></div>
  <div class="abs" style="left:194px;top:90px;width:74px"><div class="small-h">Heading Goes Here</div><div class="copy" style="margin-top:3px">Donec risus orci, gravida sit amet risus vehicula, aliquet pretium sapien. Nullam sit amet magna non ex bibendum mollis. Nunc vel neque eu augue dignissim congue ut vitae magna.</div></div>
  <div class="abs" style="left:280px;top:90px;width:74px"><div class="small-h">Heading Goes Here</div><div class="copy" style="margin-top:3px">Donec risus orci, gravida sit amet risus vehicula, aliquet pretium sapien. Nullam sit amet magna non ex bibendum mollis. Nunc vel neque eu augue dignissim congue ut vitae magna.</div></div>
  <div class="foot"><div class="mini">QK-Deck</div><div class="meta">WWW.QK-DECK-EXAMPLE.COM &nbsp;|&nbsp; ©2020 BY QK-DECK &nbsp;|&nbsp; 9</div></div>
</div>

<!-- 10 team -->
<div class="slide" style="left:26px;top:1350px">
  <div class="abs" style="left:0;top:0;width:375px;height:98px;background:linear-gradient(90deg,#0054AA,#0677BA)" role="img" aria-label="Blue-tinted warehouse background"></div>
  <div class="abs" style="left:22px;top:20px;font-size:14px;color:#fff">Meet Our <b>Team</b></div>
  <svg class="abs" width="375" height="130" viewBox="0 0 375 130" style="top:0;left:0">
    <g fill="#b7c4d1" stroke="#fff" stroke-width="2.5">
      <circle cx="53" cy="97" r="27" role="img" aria-label="Team member portrait"/>
      <circle cx="120" cy="97" r="27" role="img" aria-label="Team member portrait"/>
      <circle cx="187" cy="97" r="27" role="img" aria-label="Team member portrait"/>
      <circle cx="255" cy="97" r="27" role="img" aria-label="Team member portrait"/>
      <circle cx="322" cy="97" r="27" role="img" aria-label="Team member portrait"/>
    </g>
  </svg>
  <div class="abs" style="left:18px;top:132px;width:70px;text-align:center"><div style="font-size:6px;color:var(--mid)">Dan Holloway</div><div style="font-size:3.5px;color:#777;margin-top:3px">President</div></div>
  <div class="abs" style="left:85px;top:132px;width:70px;text-align:center"><div style="font-size:6px;color:var(--mid)">Mark Ellery</div><div style="font-size:3.5px;color:#777;margin-top:3px;line-height:1.6">mark@qk-deck-example.com<br>ext. 125</div></div>
  <div class="abs" style="left:152px;top:132px;width:70px;text-align:center"><div style="font-size:6px;color:var(--mid)">Ryan Foster</div><div style="font-size:3.5px;color:#777;margin-top:3px;line-height:1.6">ryan@qk-deck-example.com<br>ext. 126</div></div>
  <div class="abs" style="left:220px;top:132px;width:70px;text-align:center"><div style="font-size:6px;color:var(--mid)">Owen Pratt</div><div style="font-size:3.5px;color:#777;margin-top:3px;line-height:1.6">owen@qk-deck-example.com<br>ext. 124</div></div>
  <div class="abs" style="left:287px;top:132px;width:70px;text-align:center"><div style="font-size:6px;color:var(--mid)">Luke Brenner</div><div style="font-size:3.5px;color:#777;margin-top:3px;line-height:1.6">luke@qk-deck-example.com<br>ext. 128</div></div>
  <div class="foot"><div class="mini">QK-Deck</div><div class="meta">WWW.QK-DECK-EXAMPLE.COM &nbsp;|&nbsp; ©2020 BY QK-DECK &nbsp;|&nbsp; 10</div></div>
</div>

<!-- 11 workflow -->
<div class="slide" style="left:413px;top:1350px">
  <div class="heading"><b>Workflow</b> / Flowchart Slide</div>
  <svg class="abs" width="375" height="211" viewBox="0 0 375 211" style="left:0;top:0">
    <g fill="none" stroke-width="4">
      <path d="M31 114 A22 22 0 1 1 75 114" stroke="var(--blue)"/>
      <path d="M98 114 A22 22 0 1 0 142 114" stroke="var(--light)"/>
      <path d="M165 114 A22 22 0 1 1 209 114" stroke="var(--blue)"/>
      <path d="M233 114 A22 22 0 1 0 277 114" stroke="var(--light)"/>
      <path d="M300 114 A22 22 0 1 1 344 114" stroke="var(--blue)"/>
    </g>
    <circle cx="53" cy="114" r="16" fill="var(--blue)"/>
    <circle cx="120" cy="114" r="16" fill="var(--light)"/>
    <circle cx="187" cy="114" r="16" fill="var(--blue)"/>
    <circle cx="255" cy="114" r="16" fill="var(--light)"/>
    <circle cx="322" cy="114" r="16" fill="var(--blue)"/>
    <g fill="#fff">
      <circle cx="53" cy="111" r="5"/><rect x="50.5" y="116" width="5" height="4"/>
      <circle cx="116" cy="111" r="3"/><circle cx="124" cy="111" r="3"/><rect x="111" y="115" width="18" height="5" rx="2.5"/>
      <rect x="318" y="116" width="3" height="5"/><rect x="322" y="112" width="3" height="9"/><rect x="326" y="108" width="3" height="13"/>
    </g>
    <g fill="none" stroke="#fff" stroke-width="2">
      <circle cx="185" cy="112" r="5"/><line x1="189" y1="116" x2="194" y2="121"/>
      <circle cx="255" cy="114" r="6" stroke-dasharray="2 1.5" stroke-width="3"/><circle cx="255" cy="114" r="2.5"/>
    </g>
  </svg>
  <div class="abs" style="left:95px;top:58px;width:50px;text-align:center"><div style="font-size:4.5px;color:#666">Heading</div><div class="copy" style="font-size:3.3px">Nunc vel neque eu augue dignissim congue ut vitae magna. Phasellus eget commodo arcu.</div></div>
  <div class="abs" style="left:230px;top:58px;width:50px;text-align:center"><div style="font-size:4.5px;color:#666">Heading</div><div class="copy" style="font-size:3.3px">Nunc vel neque eu augue dignissim congue ut vitae magna. Phasellus eget commodo arcu.</div></div>
  <div class="abs" style="left:28px;top:146px;width:50px;text-align:center"><div style="font-size:4.5px;color:#666">Heading</div><div class="copy" style="font-size:3.3px">Nunc vel neque eu augue dignissim congue ut vitae magna. Phasellus eget commodo arcu.</div></div>
  <div class="abs" style="left:162px;top:146px;width:50px;text-align:center"><div style="font-size:4.5px;color:#666">Heading</div><div class="copy" style="font-size:3.3px">Nunc vel neque eu augue dignissim congue ut vitae magna. Phasellus eget commodo arcu.</div></div>
  <div class="abs" style="left:297px;top:146px;width:50px;text-align:center"><div style="font-size:4.5px;color:#666">Heading</div><div class="copy" style="font-size:3.3px">Nunc vel neque eu augue dignissim congue ut vitae magna. Phasellus eget commodo arcu.</div></div>
  <div class="foot"><div class="mini">QK-Deck</div><div class="meta">WWW.QK-DECK-EXAMPLE.COM &nbsp;|&nbsp; ©2020 BY QK-DECK &nbsp;|&nbsp; 11</div></div>
</div>

<!-- 12 timeline curve -->
<div class="slide" style="left:800px;top:1350px">
  <div class="heading"><b>Timeline</b> Slide</div>
  <svg class="abs" width="375" height="211" viewBox="0 0 375 211" style="left:0;top:0">
    <path d="M75 72 H310 A34 34 0 0 1 310 140 H75" fill="none" stroke="var(--line)" stroke-width="2"/>
    <circle cx="75" cy="72" r="7" fill="var(--blue)"/><circle cx="173" cy="72" r="7" fill="var(--light)"/><circle cx="272" cy="72" r="7" fill="var(--blue)"/>
    <circle cx="75" cy="140" r="7" fill="var(--light)"/><circle cx="173" cy="140" r="7" fill="var(--blue)"/><circle cx="272" cy="140" r="7" fill="var(--light)"/>
    <g fill="#fff"><rect x="72" y="69" width="6" height="6" rx="1"/><circle cx="173" cy="72" r="2.5"/><rect x="269" y="70" width="6" height="4"/><circle cx="75" cy="139" r="2.5"/><rect x="170" y="138" width="6" height="5"/><circle cx="272" cy="140" r="3" fill="none" stroke="#fff" stroke-width="1"/></g>
  </svg>
  <div class="abs" style="left:50px;top:55px;width:50px;text-align:center;font-size:4px;color:var(--blue)">2017</div>
  <div class="abs" style="left:148px;top:55px;width:50px;text-align:center;font-size:4px;color:var(--light)">2018</div>
  <div class="abs" style="left:247px;top:55px;width:50px;text-align:center;font-size:4px;color:var(--blue)">2019</div>
  <div class="abs" style="left:45px;top:82px;width:60px;text-align:center"><div style="font-size:5px;color:var(--blue)">Heading</div><div class="copy" style="font-size:3.3px">Consectetur adipiscing elit. Vivamus eu dui ex. Curabitur dapibus dignissim dui</div></div>
  <div class="abs" style="left:143px;top:82px;width:60px;text-align:center"><div style="font-size:5px;color:var(--light)">Heading</div><div class="copy" style="font-size:3.3px">Consectetur adipiscing elit. Vivamus eu dui ex. Curabitur dapibus dignissim dui</div></div>
  <div class="abs" style="left:242px;top:82px;width:60px;text-align:center"><div style="font-size:5px;color:var(--blue)">Heading</div><div class="copy" style="font-size:3.3px">Consectetur adipiscing elit. Vivamus eu dui ex. Curabitur dapibus dignissim dui</div></div>
  <div class="abs" style="left:50px;top:123px;width:50px;text-align:center;font-size:4px;color:var(--light)">2020</div>
  <div class="abs" style="left:148px;top:123px;width:50px;text-align:center;font-size:4px;color:var(--blue)">2021</div>
  <div class="abs" style="left:247px;top:123px;width:50px;text-align:center;font-size:4px;color:var(--light)">2022</div>
  <div class="abs" style="left:45px;top:150px;width:60px;text-align:center"><div style="font-size:5px;color:var(--light)">Heading</div><div class="copy" style="font-size:3.3px">Consectetur adipiscing elit. Vivamus eu dui ex. Curabitur dapibus dignissim dui</div></div>
  <div class="abs" style="left:143px;top:150px;width:60px;text-align:center"><div style="font-size:5px;color:var(--blue)">Heading</div><div class="copy" style="font-size:3.3px">Consectetur adipiscing elit. Vivamus eu dui ex. Curabitur dapibus dignissim dui</div></div>
  <div class="abs" style="left:242px;top:150px;width:60px;text-align:center"><div style="font-size:5px;color:var(--light)">Heading</div><div class="copy" style="font-size:3.3px">Consectetur adipiscing elit. Vivamus eu dui ex. Curabitur dapibus dignissim dui</div></div>
  <div class="foot"><div class="mini">QK-Deck</div><div class="meta">WWW.QK-DECK-EXAMPLE.COM &nbsp;|&nbsp; ©2020 BY QK-DECK &nbsp;|&nbsp; 12</div></div>
</div>

<!-- 13 timeline horizontal -->
<div class="slide" style="left:26px;top:1573px">
  <div class="heading"><b>Timeline</b> Slide</div>
  <svg class="abs" width="375" height="211" viewBox="0 0 375 211" style="left:0;top:0">
    <rect x="0" y="101" width="375" height="8" fill="#ececec"/>
    <g stroke="var(--light)" stroke-width=".6">
      <line x1="28" y1="105" x2="28" y2="150"/><line x1="138" y1="105" x2="138" y2="150"/><line x1="248" y1="105" x2="248" y2="150"/>
      <line x1="85" y1="105" x2="85" y2="62"/><line x1="195" y1="105" x2="195" y2="62"/>
    </g>
    <g fill="var(--blue)"><circle cx="28" cy="105" r="2.5"/><circle cx="138" cy="105" r="2.5"/><circle cx="248" cy="105" r="2.5"/></g>
    <g fill="var(--light)"><circle cx="85" cy="128" r="2"/><circle cx="195" cy="128" r="2"/></g>
  </svg>
  <div class="abs" style="left:22px;top:94px;font-size:4px;color:var(--blue);font-weight:500">2005</div>
  <div class="abs" style="left:132px;top:94px;font-size:4px;color:var(--blue);font-weight:500">2015</div>
  <div class="abs" style="left:242px;top:94px;font-size:4px;color:var(--blue);font-weight:500">2022</div>
  <div class="abs" style="left:79px;top:132px;font-size:4px;color:var(--light)">2010</div>
  <div class="abs" style="left:189px;top:132px;font-size:4px;color:var(--light)">2018</div>
  <div class="abs" style="left:88px;top:60px;width:72px"><div style="font-size:4px;color:var(--light)">Lorem ipsum dolor sit</div><div class="copy" style="font-size:3.2px">Lorem ipsum dolor sit amet, consectetur adipiscing elit, sed do eiusmod tempor incididunt labore.</div></div>
  <div class="abs" style="left:198px;top:60px;width:72px"><div style="font-size:4px;color:var(--light)">Lorem ipsum dolor sit</div><div class="copy" style="font-size:3.2px">Lorem ipsum dolor sit amet, consectetur adipiscing elit, sed do eiusmod tempor incididunt labore.</div></div>
  <div class="abs" style="left:32px;top:150px;width:72px"><div style="font-size:4px;color:var(--blue)">Lorem ipsum dolor sit</div><div class="copy" style="font-size:3.2px">Lorem ipsum dolor sit amet, consectetur adipiscing elit, sed do eiusmod tempor incididunt labore.</div></div>
  <div class="abs" style="left:142px;top:150px;width:72px"><div style="font-size:4px;color:var(--blue)">Lorem ipsum dolor sit</div><div class="copy" style="font-size:3.2px">Lorem ipsum dolor sit amet, consectetur adipiscing elit, sed do eiusmod tempor incididunt labore.</div></div>
  <div class="abs" style="left:252px;top:150px;width:72px"><div style="font-size:4px;color:var(--blue)">Lorem ipsum dolor sit</div><div class="copy" style="font-size:3.2px">Lorem ipsum dolor sit amet, consectetur adipiscing elit, sed do eiusmod tempor incididunt labore.</div></div>
  <div class="foot"><div class="mini">QK-Deck</div><div class="meta">WWW.QK-DECK-EXAMPLE.COM &nbsp;|&nbsp; ©2020 BY QK-DECK &nbsp;|&nbsp; 13</div></div>
</div>

<!-- 14 numbered steps -->
<div class="slide" style="left:413px;top:1573px">
  <div class="heading"><b>Heading</b> Goes Here</div>
  <svg class="abs" width="375" height="211" viewBox="0 0 375 211" style="left:0;top:0">
    <line x1="0" y1="80" x2="360" y2="80" stroke="var(--light)" stroke-width=".6" stroke-dasharray="2 2"/>
    <polygon points="360,78 364,80 360,82" fill="var(--light)"/>
  </svg>
  <div class="abs" style="left:52px;top:72px;width:16px;height:16px;background:var(--blue);color:#fff;font-size:9px;text-align:center;line-height:16px">1</div>
  <div class="abs" style="left:116px;top:72px;width:16px;height:16px;background:var(--light);color:#fff;font-size:9px;text-align:center;line-height:16px">2</div>
  <div class="abs" style="left:179px;top:72px;width:16px;height:16px;background:var(--blue);color:#fff;font-size:9px;text-align:center;line-height:16px">3</div>
  <div class="abs" style="left:243px;top:72px;width:16px;height:16px;background:var(--light);color:#fff;font-size:9px;text-align:center;line-height:16px">4</div>
  <div class="abs" style="left:306px;top:72px;width:16px;height:16px;background:var(--blue);color:#fff;font-size:9px;text-align:center;line-height:16px">5</div>
  <div class="abs" style="left:32px;top:94px;width:56px;text-align:center"><div style="font-size:5.5px;color:var(--blue);line-height:1.1">Heading<br>Goes Here</div><div class="copy" style="font-size:3.5px;margin-top:4px">Lorem ipsum dolor sit amet, consectetur adipiscing elit. Vivamus eu dui ex. Curabitur dapibus dignissim dui, in molestie metus feugiat sed.</div></div>
  <div class="abs" style="left:96px;top:94px;width:56px;text-align:center"><div style="font-size:5.5px;color:var(--light);line-height:1.1">Heading<br>Goes Here</div><div class="copy" style="font-size:3.5px;margin-top:4px">Lorem ipsum dolor sit amet, consectetur adipiscing elit. Vivamus eu dui ex. Curabitur dapibus dignissim dui, in molestie metus feugiat sed.</div></div>
  <div class="abs" style="left:159px;top:94px;width:56px;text-align:center"><div style="font-size:5.5px;color:var(--blue);line-height:1.1">Heading<br>Goes Here</div><div class="copy" style="font-size:3.5px;margin-top:4px">Lorem ipsum dolor sit amet, consectetur adipiscing elit. Vivamus eu dui ex. Curabitur dapibus dignissim dui, in molestie metus feugiat sed.</div></div>
  <div class="abs" style="left:223px;top:94px;width:56px;text-align:center"><div style="font-size:5.5px;color:var(--light);line-height:1.1">Heading<br>Goes Here</div><div class="copy" style="font-size:3.5px;margin-top:4px">Lorem ipsum dolor sit amet, consectetur adipiscing elit. Vivamus eu dui ex. Curabitur dapibus dignissim dui, in molestie metus feugiat sed.</div></div>
  <div class="abs" style="left:286px;top:94px;width:56px;text-align:center"><div style="font-size:5.5px;color:var(--blue);line-height:1.1">Heading<br>Goes Here</div><div class="copy" style="font-size:3.5px;margin-top:4px">Lorem ipsum dolor sit amet, consectetur adipiscing elit. Vivamus eu dui ex. Curabitur dapibus dignissim dui, in molestie metus feugiat sed.</div></div>
  <div class="foot"><div class="mini">QK-Deck</div><div class="meta">WWW.QK-DECK-EXAMPLE.COM &nbsp;|&nbsp; ©2020 BY QK-DECK &nbsp;|&nbsp; 14</div></div>
</div>

<!-- 15 chart -->
<div class="slide" style="left:800px;top:1573px">
  <div class="heading"><b>Chart</b> Slide</div>
  <svg class="abs" width="375" height="211" viewBox="0 0 375 211" style="left:0;top:0">
    <g stroke="#eee" stroke-width=".5"><line x1="32" y1="62" x2="222" y2="62"/><line x1="32" y1="78" x2="222" y2="78"/><line x1="32" y1="94" x2="222" y2="94"/><line x1="32" y1="110" x2="222" y2="110"/><line x1="32" y1="126" x2="222" y2="126"/></g>
    <line x1="32" y1="126" x2="222" y2="126" stroke="#ccc" stroke-width=".5"/>
    <g fill="var(--blue)"><rect x="46" y="83" width="5" height="43"/><rect x="90" y="82" width="5" height="44"/><rect x="134" y="96" width="5" height="30"/><rect x="178" y="82" width="5" height="44"/></g>
    <g fill="var(--mid)"><rect x="52" y="100" width="5" height="26"/><rect x="96" y="104" width="5" height="22"/><rect x="140" y="103" width="5" height="23"/><rect x="184" y="91" width="5" height="35"/></g>
    <g fill="var(--light)"><rect x="58" y="104" width="5" height="22"/><rect x="102" y="94" width="5" height="32"/><rect x="146" y="106" width="5" height="20"/><rect x="190" y="75" width="5" height="51"/></g>
    <g font-size="3" fill="#777" font-family="Ubuntu,sans-serif"><text x="49" y="132">Category 1</text><text x="93" y="132">Category 2</text><text x="137" y="132">Category 3</text><text x="181" y="132">Category 4</text>
    <text x="26" y="127">0</text><text x="26" y="111">1</text><text x="26" y="95">2</text><text x="26" y="79">3</text><text x="26" y="63">4</text></g>
    <rect x="238" y="60" width="6" height="6" fill="var(--blue)"/>
    <rect x="238" y="100" width="6" height="6" fill="var(--mid)"/>
    <rect x="238" y="140" width="6" height="6" fill="var(--light)"/>
  </svg>
  <div class="abs" style="left:250px;top:60px;width:100px"><div style="font-size:4.5px;color:var(--blue)">Heading Goes Here</div><div class="copy" style="font-size:3.3px;margin-top:3px">Lorem ipsum dolor sit amet, consectetur adipiscing elit. Vivamus eu dui ex. Curabitur dapibus dignissim dui, in molestie metus feugiat sed.</div></div>
  <div class="abs" style="left:250px;top:100px;width:100px"><div style="font-size:4.5px;color:var(--mid)">Heading Goes Here</div><div class="copy" style="font-size:3.3px;margin-top:3px">Lorem ipsum dolor sit amet, consectetur adipiscing elit. Vivamus eu dui ex. Curabitur dapibus dignissim dui, in molestie metus feugiat sed.</div></div>
  <div class="abs" style="left:250px;top:140px;width:100px"><div style="font-size:4.5px;color:var(--light)">Heading Goes Here</div><div class="copy" style="font-size:3.3px;margin-top:3px">Lorem ipsum dolor sit amet, consectetur adipiscing elit. Vivamus eu dui ex. Curabitur dapibus dignissim dui, in molestie metus feugiat sed.</div></div>
  <div class="copy abs" style="left:32px;top:148px;width:190px;font-size:3.3px">Lorem ipsum dolor sit amet, consectetur adipiscing elit. Vivamus eu dui ex. Curabitur dapibus dignissim dui, in molestie metus feugiat sed. Praesent aliquet lorem ex, eu dapibus odio varius at. Lorem ipsum dolor sit amet, consectetur adipiscing elit.</div>
  <div class="foot"><div class="mini">QK-Deck</div><div class="meta">WWW.QK-DECK-EXAMPLE.COM &nbsp;|&nbsp; ©2020 BY QK-DECK &nbsp;|&nbsp; 15</div></div>
</div>

<!-- 16 two images -->
<div class="slide" style="left:26px;top:1796px">
  <div class="heading"><b>Heading</b> Goes Here</div>
  <div class="photo" style="left:20px;top:58px;width:163px;height:72px" role="img" aria-label="Worker handling salvaged auto parts"></div>
  <div class="abs" style="left:22px;top:137px;width:160px"><div style="font-size:5px;color:var(--mid)">Heading Goes Here</div><div class="copy" style="font-size:3.5px;margin-top:2px">Lorem ipsum dolor sit amet, consectetur adipiscing elit. Vivamus eu dui ex. Curabitur dapibus dignissim dui, in molestie metus feugiat sed. Praesent aliquet lorem ex, eu dapibus odio varius at. Duis eget tellus porta, consequat lacus vitae.</div></div>
  <div class="abs" style="left:197px;top:58px;width:160px"><div style="font-size:5px;color:var(--mid)">Heading Goes Here</div><div class="copy" style="font-size:3.5px;margin-top:2px">Lorem ipsum dolor sit amet, consectetur adipiscing elit. Vivamus eu dui ex. Curabitur dapibus dignissim dui, in molestie metus feugiat sed. Praesent aliquet lorem ex, eu dapibus odio varius at.</div></div>
  <div class="photo" style="left:194px;top:101px;width:163px;height:72px" role="img" aria-label="Parts shelves stocked with boxes"></div>
  <div class="foot"><div class="mini">QK-Deck</div><div class="meta">WWW.QK-DECK-EXAMPLE.COM &nbsp;|&nbsp; ©2020 BY QK-DECK &nbsp;|&nbsp; 16</div></div>
</div>

<!-- 17 three images -->
<div class="slide" style="left:413px;top:1796px">
  <div class="heading"><b>Heading</b> Goes Here</div>
  <div class="photo cool" style="left:20px;top:58px;width:112px;height:56px" role="img" aria-label="Technician with a tablet at a parts counter"></div>
  <div class="photo cool" style="left:133px;top:58px;width:112px;height:56px;background:linear-gradient(135deg,#7e2a2a,#a8a8ad 55%,#5d6670)" role="img" aria-label="Rows of salvage vehicles in a yard"></div>
  <div class="photo" style="left:246px;top:58px;width:112px;height:56px" role="img" aria-label="Warehouse shelving with parts"></div>
  <div class="abs" style="left:22px;top:121px;width:105px"><div style="font-size:5px;color:var(--mid)">Heading Goes Here</div><div class="copy" style="font-size:3.5px;margin-top:2px;line-height:1.45">✓ Lorem ipsum dolor sit amet<br>✓ Vivamus eu dui ex<br>✓ Curabitur dapibus dignissim dui<br>✓ Praesent aliquet lorem ex, eu dapibus odio<br>✓ Duis eget tellus porta, consequat lacus<br>✓ Nulla facilisi. In et sollicitudin lacus.</div></div>
  <div class="abs" style="left:135px;top:121px;width:105px"><div style="font-size:5px;color:var(--mid)">Heading Goes Here</div><div class="copy" style="font-size:3.5px;margin-top:2px;line-height:1.45">✓ Lorem ipsum dolor sit amet<br>✓ Vivamus eu dui ex<br>✓ Curabitur dapibus dignissim dui<br>✓ Praesent aliquet lorem ex, eu dapibus odio<br>✓ Duis eget tellus porta, consequat lacus<br>✓ Nulla facilisi. In et sollicitudin lacus.</div></div>
  <div class="abs" style="left:248px;top:121px;width:105px"><div style="font-size:5px;color:var(--mid)">Heading Goes Here</div><div class="copy" style="font-size:3.5px;margin-top:2px;line-height:1.45">✓ Lorem ipsum dolor sit amet<br>✓ Vivamus eu dui ex<br>✓ Curabitur dapibus dignissim dui<br>✓ Praesent aliquet lorem ex, eu dapibus odio<br>✓ Duis eget tellus porta, consequat lacus<br>✓ Nulla facilisi. In et sollicitudin lacus.</div></div>
  <div class="foot"><div class="mini">QK-Deck</div><div class="meta">WWW.QK-DECK-EXAMPLE.COM &nbsp;|&nbsp; ©2020 BY QK-DECK &nbsp;|&nbsp; 17</div></div>
</div>

<!-- 18 image only -->
<div class="slide" style="left:800px;top:1796px">
  <div class="photo cool" style="left:20px;top:19px;width:336px;height:158px" role="img" aria-label="Technician with a tablet beside an engine on a hoist"></div>
  <div class="foot"><div class="mini">QK-Deck</div><div class="meta">WWW.QK-DECK-EXAMPLE.COM &nbsp;|&nbsp; ©2020 BY QK-DECK &nbsp;|&nbsp; 18</div></div>
</div>

<!-- 19 full image -->
<div class="slide" style="left:219px;top:2019px">
  <div class="photo" style="left:0;top:0;width:375px;height:181px" role="img" aria-label="Worker on an order picker in a tall warehouse aisle"></div>
  <div class="foot"><div class="mini">QK-Deck</div><div class="meta">WWW.QK-DECK-EXAMPLE.COM &nbsp;|&nbsp; ©2020 BY QK-DECK &nbsp;|&nbsp; 19</div></div>
</div>

<!-- 20 final -->
<div class="slide" style="left:606px;top:2019px;background:linear-gradient(135deg,#0054AA,#0677BA)" role="img" aria-label="Blue-tinted warehouse background">
  <div class="brand" style="left:38px;top:58px;font-size:18px;color:#fff">QK-Deck</div>
  <div class="abs" style="left:38px;top:95px;font-size:6px;font-weight:700;color:#fff">Contact Us</div>
  <div class="abs" style="left:38px;top:106px;font-size:4px;color:#fff">480 Harbor Ave. Springdale Ohio 45000</div>
  <svg class="abs" width="10" height="40" viewBox="0 0 10 40" style="left:38px;top:117px" fill="none" stroke="#fff" stroke-width=".8">
    <path d="M1.5 1.5 Q1.5 7 6.5 7 L6.5 5 L4.5 4.5 L4 5.5 Q2.8 5 2.5 3.5 L3.5 3 L3 1 Z"/>
    <rect x="1" y="12" width="6" height="4.5"/><path d="M1 12 L4 14.5 L7 12"/>
    <circle cx="4" cy="25" r="3"/><line x1="1" y1="25" x2="7" y2="25"/><line x1="4" y1="22" x2="4" y2="28"/>
  </svg>
  <div class="abs" style="left:50px;top:117px;font-size:4px;color:#fff;line-height:2.6">555-014-0100<br>support@qk-deck-example.com<br>www.qk-deck-example.com</div>
  <div class="abs" style="left:172px;top:199px;font-size:3px;color:#fff">©2020 by QK-Deck</div>
</div>

</body>
</html>
```